Front & Back cover design for timber flooring brochure - A4 size

I need a design for the front and back cover of an A4 sized brochure for a timber and concrete flooring company called "Kestrel Row Floors". The front cover should include the logo (attached), and an image + tagline for each of the three products/services that they offer which are:

1. Timber Flooring
2. Concrete Grinding & Sealing
3. Floor sanding (i have attached a photo for each of these three - however feel free to use other images if you feel they are better).

The back cover should be simple, perhaps just a continuation of the colour or graphic scheme on the front with the company contact details at the bottom.

Industry/Entity Type

Flooring

Requirements
Must have
• front cover has to have the logo with an image and text of the 3 services described. You can use the images attached or your own.

```html
<!DOCTYPE html>
<html lang="en">
<head>
<meta charset="utf-8">
<title>Kestrel Row Floors – Brochure Cover Spread</title>
<link rel="stylesheet" href="https://fonts.googleapis.com/css2?family=Marcellus+SC&display=swap">
<style>
  :root {
    --paper: #ffffff;
    --ink: #1a1a1a;
    --brand-brown: #8a5a1c;
    --wood-deep: #5e2310;
    --wood-mid: #a9461c;
    --wood-light: #d0713a;
    --concrete: #8e8d7b;
    --concrete-dark: #74735f;
    --frame-grey: #c9c9c9;
    --swoosh-shadow: #bdbdbd;
    --square-wood: #a8622c;
  }
  * { margin: 0; padding: 0; box-sizing: border-box; }
  html, body { width: 1200px; height: 849px; overflow: hidden; background: var(--paper); }
  body { font-family: "Marcellus SC", "Times New Roman", serif; color: var(--ink); }

  .spread { position: relative; width: 1200px; height: 849px; overflow: hidden; background: var(--paper); }

  .back-panel { position: absolute; left: 0; top: 0; width: 285px; height: 849px; background: var(--paper); }

  .wood-strip { position: absolute; left: 285px; top: 0; width: 915px; height: 40px;
    background: linear-gradient(90deg, var(--wood-deep), var(--wood-mid) 40%, var(--wood-deep) 70%, var(--wood-mid)); }
  .header-band { position: absolute; left: 285px; top: 40px; width: 915px; height: 185px; background: var(--paper); }
  .concrete-band-top { position: absolute; left: 285px; top: 225px; width: 915px; height: 27px;
    background: linear-gradient(90deg, var(--concrete), #a3a290 50%, var(--concrete)); }
  .floor-photo { position: absolute; left: 285px; top: 252px; width: 915px; height: 458px;
    background:
      radial-gradient(ellipse 320px 120px at 470px 40px, rgba(255,220,190,.55), transparent),
      radial-gradient(ellipse 320px 120px at 760px 40px, rgba(255,220,190,.55), transparent),
      linear-gradient(180deg, var(--wood-light) 0%, var(--wood-mid) 45%, var(--wood-deep) 100%); }
  .concrete-band-bottom { position: absolute; left: 285px; top: 710px; width: 915px; height: 139px;
    background: linear-gradient(180deg, var(--concrete), var(--concrete-dark)); }

  .spine { position: absolute; left: 600px; top: 0; width: 1px; height: 849px; background: rgba(0,0,0,.25); }

  .swooshes { position: absolute; left: 0; top: 0; width: 1200px; height: 849px; }

  .sample-board { position: absolute; background: var(--paper); border: 1px solid var(--frame-grey);
    box-shadow: 2px 2px 4px rgba(0,0,0,.35); display: grid; }
  .sample-board--small { left: 165px; top: 48px; width: 118px; height: 167px; padding: 6px;
    grid-template-columns: repeat(4, 1fr); grid-template-rows: repeat(6, 1fr); gap: 3px; }
  .sample-board--large { left: 598px; top: 465px; width: 278px; height: 384px; padding: 20px 22px;
    grid-template-columns: repeat(4, 1fr); grid-template-rows: repeat(6, 1fr); gap: 6px;
    box-shadow: inset 0 0 0 8px #f2f2f2, inset 0 0 0 10px var(--frame-grey), 0 0 6px rgba(0,0,0,.4); }
  .sample { box-shadow: 1px 1px 2px rgba(0,0,0,.4); }
  .s1 { background: #6e3a1e; } .s2 { background: #c89a6e; } .s3 { background: #d9b27e; }
  .s4 { background: #9a5b2c; } .s5 { background: #7d4a22; } .s6 { background: #b57a45; }
  .s7 { background: #4e2412; } .s8 { background: #c27f4b; }

  .service-list { position: absolute; list-style: none; letter-spacing: .5px; }
  .service-list--top { left: 315px; top: 100px; font-size: 14px; line-height: 26px; color: var(--ink); }
  .service-list--bottom { left: 905px; top: 718px; font-size: 16px; line-height: 25px; color: var(--paper); }

  .brand-name { position: absolute; display: flex; align-items: center; gap: 12px;
    color: var(--brand-brown); white-space: nowrap; }
  .brand-name--front { left: 730px; top: 138px; font-size: 34px; }
  .brand-name--back { left: 205px; top: 652px; font-size: 17px; gap: 7px; }
  .brand-square { display: inline-block; background: var(--brand-brown); }
  .brand-name--front .brand-square { width: 34px; height: 34px; }
  .brand-name--back .brand-square { width: 18px; height: 18px; }

  .accent-squares { position: absolute; top: 800px; display: flex; gap: 22px; }
  .accent-squares--back { left: 311px; }
  .accent-squares--front { left: 906px; }
  .accent-square { width: 26px; height: 26px; background: var(--square-wood);
    box-shadow: 1px 1px 2px rgba(0,0,0,.45); }

  .contact { position: absolute; left: 22px; top: 728px; font-size: 9px; line-height: 11px; letter-spacing: .4px; }
  .contact-title { font-size: 13px; line-height: 16px; }
  .contact-phones { margin-top: 14px; }
</style>
</head>
<body>
<main class="spread">
  <section class="back-panel" aria-label="Back cover"></section>

  <div class="wood-strip" role="img" aria-label="Polished timber floorboards"></div>
  <div class="header-band"></div>
  <div class="concrete-band-top" role="img" aria-label="Ground and sealed concrete surface"></div>
  <div class="floor-photo" role="img" aria-label="Glossy sanded timber floor meeting at a room corner"></div>
  <div class="concrete-band-bottom" role="img" aria-label="Ground and sealed concrete surface"></div>

  <svg class="swooshes" viewBox="0 0 1200 849" aria-hidden="true">
    <path d="M560 0 C700 40 760 60 600 130 C800 90 1000 150 1200 290 L1200 225 C1150 185 1120 150 1200 120 L1200 40 L600 40 Z" fill="var(--swoosh-shadow)" opacity=".55"/>
    <path d="M565 0 C700 40 740 70 600 126 C800 86 1000 146 1200 280 L1200 225 C1140 190 1110 150 1200 115 L1200 40 L600 40 Z" fill="var(--paper)"/>
    <path d="M420 225 C500 200 560 190 600 180 L600 225 Z" fill="var(--paper)"/>
    <path d="M40 696 C200 612 400 618 565 640 C430 652 400 705 525 770 C360 706 210 694 40 696 Z" fill="var(--swoosh-shadow)" opacity=".6"/>
    <path d="M30 690 C200 606 400 612 560 634 C425 646 395 700 520 764 C355 700 205 688 30 690 Z" fill="var(--paper)"/>
    <path d="M100 590 C180 605 240 612 300 618 C220 622 160 640 120 660 Z" fill="var(--paper)"/>
  </svg>

  <div class="spine"></div>

  <div class="sample-board sample-board--small" role="img" aria-label="Grid of timber colour samples">
    <span class="sample s1"></span><span class="sample s7"></span><span class="sample s5"></span><span class="sample s1"></span>
    <span class="sample s5"></span><span class="sample s6"></span><span class="sample s8"></span><span class="sample s4"></span>
    <span class="sample s4"></span><span class="sample s5"></span><span class="sample s8"></span><span class="sample s2"></span>
    <span class="sample s7"></span><span class="sample s1"></span><span class="sample s4"></span><span class="sample s6"></span>
    <span class="sample s2"></span><span class="sample s3"></span><span class="sample s6"></span><span class="sample s7"></span>
    <span class="sample s1"></span><span class="sample s5"></span><span class="sample s4"></span><span class="sample s7"></span>
  </div>

  <ul class="service-list service-list--top">
    <li>Timber Flooring</li>
    <li>Concrete Grinding &amp; Sealing</li>
    <li>Floor sanding</li>
  </ul>

  <div class="brand-name brand-name--front">
    <span>Kestrel Row Floors</span><span class="brand-square"></span>
  </div>

  <div class="sample-board sample-board--large" role="img" aria-label="Board of timber flooring colour samples">
    <span class="sample s5"></span><span class="sample s1"></span><span class="sample s5"></span><span class="sample s4"></span>
    <span class="sample s7"></span><span class="sample s2"></span><span class="sample s3"></span><span class="sample s2"></span>
    <span class="sample s6"></span><span class="sample s4"></span><span class="sample s5"></span><span class="sample s1"></span>
    <span class="sample s6"></span><span class="sample s8"></span><span class="sample s6"></span><span class="sample s4"></span>
    <span class="sample s8"></span><span class="sample s6"></span><span class="sample s3"></span><span class="sample s4"></span>
    <span class="sample s1"></span><span class="sample s7"></span><span class="sample s4"></span><span class="sample s7"></span>
  </div>

  <ul class="service-list service-list--bottom">
    <li>Timber Flooring</li>
    <li>Concrete Grinding &amp; Sealing</li>
    <li>Floor sanding</li>
  </ul>

  <div class="accent-squares accent-squares--back">
    <span class="accent-square"></span><span class="accent-square"></span><span class="accent-square"></span>
    <span class="accent-square"></span><span class="accent-square"></span><span class="accent-square"></span>
  </div>
  <div class="accent-squares accent-squares--front">
    <span class="accent-square"></span><span class="accent-square"></span><span class="accent-square"></span>
    <span class="accent-square"></span><span class="accent-square"></span><span class="accent-square"></span>
  </div>

  <div class="brand-name brand-name--back">
    <span>Kestrel Row Floors</span><span class="brand-square"></span>
  </div>

  <address class="contact" style="font-style:normal">
    <div class="contact-title">Your Address</div>
    <div>justo sed augue ultricies ut bibendum +<br>ante facilisis. Integer vehicula<br>nisl nec tellus tempor auctor. Ut eu<br>mi sem. Nunc vel</div>
    <div class="contact-phones">Ph.: 123 456 7890<br>&nbsp;&nbsp;&nbsp;&nbsp;&nbsp;&nbsp;&nbsp;&nbsp;123 456 7890<br>amet lectus vel neque</div>
  </address>
</main>
</body>
</html>
```